Dentist logo, business card and website

I have done an amateur job of creating a logo, business card and website. I would like it to look more professional. the current website can be found at www.tobenkarsh.com - I would like the website to be built and run through wix.com. The content on the website is as I would like it but I am open to suggestions.

The logo should be simple, may be best to keep to the letter TK - maybe to look like the V is a reflection of the A? Again, I am open to suggestions (I have attached a couple of images I have used on presentations but I would like the logo that you design to have a 'no fill' background so it can be placed on slides (for presentations etc).

The colour scheme seems wrong for a dentist, perhaps duck egg with black writing would be better? This applies to the business card as well (I have attached a PDF of some I have had made in the past but again they look amateur and colour scheme is wrong. The business cards should be landscape, have the logo in the top right corner, my name and qualifications in the middle, and my website and physical address in the bottom left corner: Glenmorrow Dental Surgery, 41-43 Pellow Crescent, Cardiff CF22 9RW.

Target Market(s)

30-60 year olds

Industry/Entity Type

Dental

Contact Information for Business Card

Please see brief and uploads.

Logo Text

TK

Number of Pages Required

4 page

Font styles to use
Decorative
Script

Requirements
Must have
• A sophisticated mature feel.
Nice to have
• Simplicity.
Should not have
• Anything too complicated.

```html
<!DOCTYPE html>
<html lang="en">
<head>
<meta charset="utf-8">
<title>Toben Karsh – Restorative and Implant Dentist</title>
<link rel="stylesheet" href="https://fonts.googleapis.com/css2?family=Cinzel:wght@400;700&family=Open+Sans:ital,wght@0,400;0,700;1,400&display=swap">
<style>
:root{
  --ink:#222222;
  --header:#2b2a28;
  --panel:#252423;
  --gold:#a2865a;
  --gold-dark:#8f7449;
  --duck:#dde7e4;
  --white:#ffffff;
  --muted:#8d8d8d;
  --field:#cfd8d5;
}
*{box-sizing:border-box;margin:0;padding:0}
html,body{width:1200px;height:3564px;overflow:hidden}
body{position:relative;background:var(--duck);font-family:"Open Sans",Arial,sans-serif;color:var(--ink)}
.abs{position:absolute}
.serif{font-family:"Cinzel",Georgia,serif;font-weight:400}

/* header */
.site-header{left:0;top:0;width:1200px;height:86px;background:var(--header)}
.brand{left:71px;top:14px}
.brand-name{font-family:"Cinzel",Georgia,serif;font-size:28px;color:var(--gold);letter-spacing:1px;display:flex;align-items:center;gap:10px}
.brand-dot{width:12px;height:12px;border-radius:50%;background:var(--gold)}
.brand-quals{font-family:"Cinzel",Georgia,serif;font-size:10px;color:var(--gold);letter-spacing:1px;margin-left:22px;margin-top:2px}
.nav a{position:absolute;top:32px;font-family:"Cinzel",Georgia,serif;font-size:15px;color:var(--white);text-decoration:none;white-space:nowrap}
.btn-gold{background:var(--gold);color:var(--white);font-family:"Cinzel",Georgia,serif;font-size:13px;display:flex;align-items:center;justify-content:center;letter-spacing:.5px}
.nav-cta{left:981px;top:26px;width:188px;height:36px}

/* hero */
.hero{left:0;top:86px;width:1200px;height:615px;background:linear-gradient(100deg,#6c9ab8 0%,#9cbccf 22%,#d8b8a4 45%,#e6c8b6 62%,#cfd9e4 82%,#a9c2d6 100%)}
.hero-title{left:86px;top:460px;font-size:31px;line-height:42px;color:var(--white)}
.hero-cta{left:86px;top:565px;width:236px;height:48px;font-size:15px}
.scroll-label{left:1140px;top:330px;transform:rotate(90deg);transform-origin:left top;font-size:11px;letter-spacing:3px;color:var(--white)}

/* welcome band */
.welcome{left:0;top:701px;width:1200px;height:154px;background:var(--gold);text-align:center;color:var(--white)}
.welcome h1{font-family:"Cinzel",Georgia,serif;font-weight:400;font-size:40px;margin-top:30px;letter-spacing:1px}
.welcome h2{font-family:"Cinzel",Georgia,serif;font-weight:400;font-size:28px;margin-top:4px;letter-spacing:1px}

/* about */
.about-photo{left:0;top:855px;width:599px;height:459px;background:linear-gradient(120deg,#c9a99b 0%,#efe1da 40%,#f6efec 65%,#c7b3ad 100%)}
.about-panel{left:599px;top:855px;width:601px;height:459px;background:var(--panel)}
.about-title{left:708px;top:955px;font-size:40px;color:var(--white);letter-spacing:1px}
.about-text{left:708px;top:1030px;width:456px;font-size:12.5px;line-height:24px;color:var(--muted)}
.btn-outline{left:708px;top:1164px;width:171px;height:43px;border:1px solid var(--gold);color:var(--gold);font-family:"Cinzel",Georgia,serif;font-size:13px;display:flex;align-items:center;justify-content:center}

/* services */
.services-title{left:0;top:1414px;width:1200px;text-align:center;font-size:40px;letter-spacing:1px}
.services-intro{left:180px;top:1494px;width:840px;text-align:center;font-size:12.5px;line-height:24px;color:#333}
.card{width:300px}
.card-photo{width:300px;height:238px}
.card-cap{width:300px;height:83px;background:var(--gold);text-align:center;color:var(--white);padding-top:14px}
.card-cap h3{font-family:"Cinzel",Georgia,serif;font-weight:400;font-size:19px;letter-spacing:1px}
.card-cap p{font-size:11.5px;margin-top:6px;display:flex;align-items:center;justify-content:center;gap:5px}

/* testimonials */
.testimonials{left:0;top:2411px;width:1200px;height:628px;background:linear-gradient(110deg,#3b3430 0%,#5a4a40 35%,#4d4039 60%,#3a332f 100%)}
.testi-title{left:0;top:2488px;width:1200px;text-align:center;font-size:40px;color:var(--white);letter-spacing:1px}
.quote{left:190px;top:2582px;width:855px;text-align:center;font-style:italic;font-size:16.5px;line-height:33px;color:#ece6e1}
.qmark{font-family:Georgia,serif;font-size:60px;color:#9c9590;line-height:1}
.avatar{left:551px;top:2815px;width:96px;height:96px;border-radius:50%;background:linear-gradient(#b68d74,#7c5a48);border:3px solid #d8d0ca}
.author{left:0;top:2938px;width:1200px;text-align:center;font-size:16px;color:#ddd}
.author b{color:var(--white)}

/* footer */
.practice-name{left:188px;top:3122px;font-size:20px;letter-spacing:1px}
.contact-lines{left:188px;top:3164px;font-size:12px;line-height:24px;color:#333}
.socials{left:186px;top:3272px;display:flex;gap:6px}
.socials span{width:32px;height:32px;border-radius:50%;background:var(--gold)}
.foot-brand{left:188px;top:3350px}
.foot-brand .brand-name{font-size:34px}
.foot-brand .brand-quals{font-size:12px;margin-left:24px}
.touch-title{left:658px;top:3108px;font-size:40px;letter-spacing:1px}
.field{left:658px;width:352px;height:36px;border:1px solid #c5cfcc;background:var(--duck);font-size:11px;color:#444;padding:10px 12px}
.send{left:658px;top:3421px;width:98px;height:34px;font-size:13px}
.rule{left:0;top:3493px;width:1200px;height:1px;background:#cfd8d5}
.copyright{left:0;top:3512px;width:1200px;text-align:center;font-size:11.5px;color:#444}
</style>
</head>
<body>

<header class="abs site-header">
  <div class="abs brand">
    <div class="brand-name"><span class="brand-dot"></span>Toben Karsh</div>
    <div class="brand-quals">BDS (Hons) MJDF RCS (Eng)</div>
  </div>
  <nav class="nav">
    <a style="left:394px">About Me</a>
    <a style="left:527px">Testimonials</a>
    <a style="left:684px">Patient Resources</a>
    <a style="left:879px">Contact</a>
  </nav>
  <div class="abs btn-gold nav-cta">Get an Appointment</div>
</header>

<section class="abs hero" role="img" aria-label="Photo of a smiling patient having her teeth examined with a dental mirror"></section>
<h1 class="abs serif hero-title">I am a Restorative and<br>implant dentist based in Cardiff</h1>
<div class="abs btn-gold hero-cta">Get an Appointment</div>
<div class="abs scroll-label">SCROLL</div>

<section class="abs welcome">
  <h1>Welcome to TobenKarsh</h1>
  <h2>I am a restorative and implant dentist based in Cardiff</h2>
</section>

<div class="abs about-photo" role="img" aria-label="Close-up photo of a patient receiving dental treatment"></div>
<div class="abs about-panel"></div>
<h2 class="abs serif about-title">About Toben Karsh</h2>
<p class="abs about-text">I provide care for my patients at Glenmorrow Dental Surgery, a state of the art private practice in Glenmorrow Village, Cardiff. I have a particular interest in periodontal disease and in restoring missing teeth with dental implants.</p>
<div class="abs btn-outline">Read More Info</div>

<h2 class="abs serif services-title">What We Do</h2>
<p class="abs services-intro">I provide care for my patients at Glenmorrow Dental Surgery, a state of the art private practice in Glenmorrow Village, Cardiff. I have a particular interest in periodontal disease and in restoring missing teeth with dental implants.</p>

<div class="abs card" style="left:116px;top:1594px">
  <div class="card-photo" role="img" aria-label="Photo of a woman holding her jaw in pain" style="background:linear-gradient(135deg,#f0d4c8,#d9967f 60%,#c4766a)"></div>
  <div class="card-cap"><h3>Periodontal Disease</h3><p>Click here for view information <svg width="10" height="10" viewBox="0 0 10 10"><circle cx="5" cy="5" r="5" fill="#fff"/><path d="M4 2.8 6.2 5 4 7.2" stroke="#a2865a" stroke-width="1.4" fill="none"/></svg></p></div>
</div>
<div class="abs card" style="left:451px;top:1594px">
  <div class="card-photo" role="img" aria-label="Photo of a dental implant model held in hands" style="background:linear-gradient(135deg,#5b3f33,#b08c73 50%,#d9c6b6)"></div>
  <div class="card-cap"><h3>Dental Implants</h3><p>Click here for view information <svg width="10" height="10" viewBox="0 0 10 10"><circle cx="5" cy="5" r="5" fill="#fff"/><path d="M4 2.8 6.2 5 4 7.2" stroke="#a2865a" stroke-width="1.4" fill="none"/></svg></p></div>
</div>
<div class="abs card" style="left:784px;top:1594px">
  <div class="card-photo" role="img" aria-label="Photo of a smiling patient in the dental chair" style="background:linear-gradient(135deg,#8a5a3c,#d49b78 45%,#7fb3cf)"></div>
  <div class="card-cap"><h3>General Dental</h3><p>Click here for view information <svg width="10" height="10" viewBox="0 0 10 10"><circle cx="5" cy="5" r="5" fill="#fff"/><path d="M4 2.8 6.2 5 4 7.2" stroke="#a2865a" stroke-width="1.4" fill="none"/></svg></p></div>
</div>

<div class="abs card" style="left:116px;top:1970px">
  <div class="card-photo" role="img" aria-label="Photo of a dental laboratory with a jaw model" style="background:linear-gradient(135deg,#c9d3d8,#e9e4e0 50%,#b2443d)"></div>
  <div class="card-cap"><h3>Clinical Research</h3><p>Click here for view information <svg width="10" height="10" viewBox="0 0 10 10"><circle cx="5" cy="5" r="5" fill="#fff"/><path d="M4 2.8 6.2 5 4 7.2" stroke="#a2865a" stroke-width="1.4" fill="none"/></svg></p></div>
</div>
<div class="abs card" style="left:451px;top:1970px">
  <div class="card-photo" role="img" aria-label="Photo of a dentist treating a patient" style="background:linear-gradient(135deg,#e8e8e6,#b7a89c 50%,#6e5a4e)"></div>
  <div class="card-cap"><h3>Teeth Replacement</h3><p>Click here for view information <svg width="10" height="10" viewBox="0 0 10 10"><circle cx="5" cy="5" r="5" fill="#fff"/><path d="M4 2.8 6.2 5 4 7.2" stroke="#a2865a" stroke-width="1.4" fill="none"/></svg></p></div>
</div>
<div class="abs card" style="left:784px;top:1970px">
  <div class="card-photo" role="img" aria-label="Photo of a patient wearing a sedation nasal mask" style="background:linear-gradient(135deg,#7aa7d6,#e1cfc4 50%,#c6417a)"></div>
  <div class="card-cap"><h3>Sedation Dentistry</h3><p>Click here for view information <svg width="10" height="10" viewBox="0 0 10 10"><circle cx="5" cy="5" r="5" fill="#fff"/><path d="M4 2.8 6.2 5 4 7.2" stroke="#a2865a" stroke-width="1.4" fill="none"/></svg></p></div>
</div>

<section class="abs testimonials" role="img" aria-label="Dimmed background photo of a smiling family"></section>
<h2 class="abs serif testi-title">Testimonials</h2>
<span class="abs qmark" style="left:152px;top:2568px">&ldquo;</span>
<p class="abs quote">Dr Toben Karsh has been my dentist for several years now, I can quite confidently say that he is one of the most outstanding professionals I have encountered, not just in the medical world, but in all walks of life. As an international opera singer, my teeth are very important to me, both their appearance and function, and Toben's brilliance and skill in their care is a source of great reassurance. In addition to his professional virtuosity, Toben is an exceptional person, endlessly kind, witty and interested in his patients. I am proud to give him my highest possible recommendation.</p>
<span class="abs qmark" style="left:1022px;top:2740px">&rdquo;</span>
<div class="abs avatar" role="img" aria-label="Portrait photo of the reviewer"></div>
<p class="abs author"><b>- MARTIN -</b> London</p>

<h3 class="abs serif practice-name">Glenmorrow Dental Surgery</h3>
<div class="abs contact-lines">
  41-43 Pellow Crescent, Cardiff CF22 9RW.<br>
  Email Us : info@tobenkarsh.com<br>
  Call Us : 029 2048 7310
</div>
<div class="abs socials" aria-label="Social links"><span></span><span></span><span></span><span></span><span></span></div>
<div class="abs foot-brand">
  <div class="brand-name"><span class="brand-dot"></span>Toben Karsh</div>
  <div class="brand-quals">BDS (Hons) MJDF RCS (Eng)</div>
</div>

<h2 class="abs serif touch-title">Get In Touch</h2>
<div class="abs field" style="top:3181px">Name</div>
<div class="abs field" style="top:3234px">Email</div>
<div class="abs field" style="top:3286px">Phone</div>
<div class="abs field" style="top:3336px;height:70px">Message</div>
<div class="abs btn-gold send">Send</div>

<div class="abs rule"></div>
<p class="abs copyright">© 2017. TobenKarsh. All rights reserved.</p>

</body>
</html>
```